Double-sided business card needed - specific brief

We need a double sided business card designed for our company Radiant Trimline. Having lost a lot of weight myself, the back of the card needs to show my before and after pictures. It needs to cover the entire back side of the card. This might be with my two before pictures over set on top of my main after picture or in separate frames. I'll leave that to your artistic consideration. The front needs to have our logo with contact details centred below.

The cards will be printed by PRINTKO.com and will be rectangular, 84mm x 55mm, but with ROUNDED edges. Please therefore present your designs rectangular but with rounded edges if possible.

The card should be designed in LANDSCAPE orientation.

As well as the logo, the front of the card should have the following details:

Moira Blakewell
Weight Loss Motivator with 189lb personal loss
moira@radiant-trimline.example
+44 (0)7700 900418

The website is important so should perhaps be more bold than the rest:
www.radiant-trimline.example

My brand colours are: Pink #CD2366, Light Pink #FD88AD. Blue #1C9CB1, Light Blue #64C4DE

Target Market(s)

Women 30+

Contact Information for Business Card

As description above

Font styles to use
Sans Serif

Requirements
Must have
• Double sided.
• Back side entirely covered with my before and after pictures.
• You may wish to float my before pictures on top of my after picture or add them in different frames. I look forward to seeing your different suggestions.

```html
<!DOCTYPE html>
<html lang="en">
<head>
<meta charset="utf-8">
<title>Radiant Trimline – Business Card</title>
<link rel="stylesheet" href="https://fonts.googleapis.com/css2?family=Roboto+Condensed:wght@400;700&display=swap">
<style>
  :root {
    --pink: #CD2366;
    --pink-light: #FD88AD;
    --pink-wash: #f3d7e1;
    --blue: #1C9CB1;
    --blue-light: #64C4DE;
    --ground: #e4e4e4;
    --card-white: #fbfbfb;
  }
  * { box-sizing: border-box; margin: 0; padding: 0; }
  html, body { width: 1200px; height: 862px; overflow: hidden; }
  body {
    background: var(--ground);
    font-family: "Roboto Condensed", Arial, sans-serif;
    position: relative;
  }
  .card {
    position: absolute;
    top: 261px;
    width: 520px;
    height: 340px;
    border-radius: 22px;
    overflow: hidden;
    box-shadow: 0 6px 18px rgba(0,0,0,0.18);
  }
  .card--back { left: 60px; }
  .card--front {
    left: 620px;
    background:
      radial-gradient(circle at 70% 0%, var(--pink-wash) 0%, rgba(243,215,225,0.55) 35%, var(--card-white) 75%);
  }
  .card--back svg { display: block; }

  .brand {
    position: absolute;
    left: 36px;
    top: 168px;
    display: flex;
    align-items: center;
    gap: 10px;
  }
  .brand__dot {
    width: 20px; height: 20px;
    border-radius: 50%;
    background: var(--pink);
    flex: none;
  }
  .brand__name {
    font-size: 24px;
    font-weight: 700;
    color: var(--pink);
    letter-spacing: 0.5px;
    line-height: 1.05;
    text-transform: uppercase;
  }

  .holder {
    position: absolute;
    right: 34px;
    top: 34px;
    text-align: right;
  }
  .holder__name {
    font-size: 34px;
    font-weight: 700;
    color: var(--blue);
    line-height: 1.05;
  }
  .holder__role {
    font-size: 13px;
    font-weight: 700;
    color: var(--pink);
    margin-top: 4px;
  }

  .contacts {
    position: absolute;
    left: 236px;
    top: 148px;
    list-style: none;
  }
  .contacts__item {
    display: flex;
    align-items: center;
    gap: 10px;
    font-size: 14px;
    font-weight: 700;
    color: var(--blue);
    margin-bottom: 12px;
    white-space: nowrap;
  }
  .contacts__icon { width: 22px; height: 22px; flex: none; }

  .website {
    position: absolute;
    right: 34px;
    bottom: 46px;
    font-size: 21px;
    font-weight: 700;
    color: var(--blue);
    letter-spacing: 0.5px;
  }
</style>
</head>
<body>

  <section class="card card--back" aria-label="Card back: before and after photos">
    <svg width="520" height="340" viewBox="0 0 520 340">
      <rect class="photo-after" x="0" y="0" width="520" height="340" fill="#8a6a58" role="img" aria-label="After photo: slim woman seated on a sofa in a navy jumper and jeans"/>
      <polygon points="300,0 520,0 520,340 260,340 230,150" fill="#3b3f5c" role="img" aria-label="After photo detail: woman in navy jumper seated on a leather sofa"/>
      <polygon points="0,70 150,55 215,150 260,340 0,340" fill="var(--pink-light)"/>
      <polygon points="6,76 148,62 208,152 252,340 0,340 0,78" fill="#7a8a5a" role="img" aria-label="Before photo: woman in a white jacket holding a dog in a garden"/>
      <polygon points="120,38 295,10 318,118 210,150 165,110" fill="var(--pink-light)"/>
      <polygon points="128,44 290,18 310,112 212,142 170,106" fill="#b8a796" role="img" aria-label="Before photo: woman wearing a bridal veil"/>
    </svg>
  </section>

  <section class="card card--front" aria-label="Card front: logo and contact details">
    <div class="brand">
      <span class="brand__dot"></span>
      <span class="brand__name">Radiant<br>Trimline</span>
    </div>

    <div class="holder">
      <h1 class="holder__name">Moira Blakewell</h1>
      <p class="holder__role">Weight Loss Motivator with 189lb personal loss</p>
    </div>

    <ul class="contacts">
      <li class="contacts__item">
        <svg class="contacts__icon" viewBox="0 0 24 24" aria-hidden="true">
          <rect x="2" y="5" width="20" height="14" fill="none" stroke="var(--pink)" stroke-width="2"/>
          <polyline points="2,5 12,13 22,5" fill="none" stroke="var(--pink)" stroke-width="2"/>
        </svg>
        moira@radiant-trimline.example
      </li>
      <li class="contacts__item">
        <svg class="contacts__icon" viewBox="0 0 24 24" aria-hidden="true">
          <path d="M6.6 10.8a15 15 0 0 0 6.6 6.6l2.2-2.2a1 1 0 0 1 1-.25 11.4 11.4 0 0 0 3.6.57 1 1 0 0 1 1 1V20a1 1 0 0 1-1 1A17 17 0 0 1 3 4a1 1 0 0 1 1-1h3.5a1 1 0 0 1 1 1c0 1.25.2 2.450.57 3.57a1 1 0 0 1-.25 1z" fill="none" stroke="var(--pink)" stroke-width="1.8"/>
        </svg>
        +44 (0)7700 900418
      </li>
    </ul>

    <p class="website">www.radiant-trimline.example</p>
  </section>

</body>
</html>
```